Menu Board 1000mmx500mm re-design

I would like to re-design exiting menu board 1000mmx500mm. Current board letters are bit to small to read. I would like to have pictures (attached) of the food offered on it and at the same time to create balance between pictures and size of the text to be easily readable. Fonts and colours are up to designer choice but prefer warm and bright colours rather anything dark.

Target Market(s)

Food industry

Industry/Entity Type

Food

Font styles to use
Other font styles liked:
• I leave font choice to designer

Colors
FFC000
F8CF3A
FAE287
FDF2CF
FEFAEE
F0912C
F2A743
F7CA91
FBE8D2
FDF5EE
EE7325
F08F49
F5BC92
FAE3D3
FDF4ED

Requirements
Must have
• Pictures + Text
Nice to have
• Balance between images and text.
Should not have
• Can't think of any

```html
<!DOCTYPE html>
<html lang="en">
<head>
<meta charset="utf-8">
<title>Menu Board</title>
<link href="https://fonts.googleapis.com/css2?family=League+Spartan:wght@800&family=Fjalla+One&family=Didact+Gothic&display=swap" rel="stylesheet">
<style>
  :root {
    --orange: #EE7325;
    --orange-soft: #F08F49;
    --peach: #F5BC92;
    --cream: #FDF4ED;
    --board: #f1f0ed;
    --board-edge: #e4e2de;
    --ink: #1d1b1a;
    --white: #ffffff;
    --stage: #ece9e4;
  }
  * { margin: 0; padding: 0; box-sizing: border-box; }
  html, body { width: 1200px; height: 848px; overflow: hidden; background: var(--stage); }
  .menu-board {
    position: absolute; left: 400px; top: 22px; width: 400px; height: 804px;
    background: linear-gradient(90deg, var(--board) 0%, #f7f6f4 40%, var(--board) 70%, #f6f5f3 100%);
    box-shadow: 0 2px 10px rgba(0,0,0,.12);
    overflow: hidden;
  }
  .photo { position: absolute; }
  .hero-photo {
    left: 120px; top: 0; width: 280px; height: 272px;
  }
  .dish-photo {
    width: 78px; height: 78px; border-radius: 50%;
    border: 3px solid var(--white); outline: 2px solid var(--orange);
  }
  .photo-potatoes { left: 74px; top: 24px; background: radial-gradient(circle at 40% 40%, #f3b04a, #b8621d); }
  .photo-ciabatta { left: 72px; top: 108px; background: linear-gradient(180deg, #e9d8b8 0%, #d9b27a 35%, #3f7a2c 50%, #c99a5e 65%, #a8703e 100%); }
  .photo-wrap { left: 125px; top: 175px; background: radial-gradient(circle at 50% 50%, #e8d8c3, #b98d6a); }
  .photo-roast { left: 208px; top: 198px; background: radial-gradient(circle at 50% 45%, #e6a24a, #8a4a1c); }
  .photo-chicken { left: 296px; top: 182px; background: radial-gradient(circle at 45% 50%, #d8913f, #6e3a1a); }
  .photo-arc { position: absolute; left: 0; top: 0; }

  .brush { position: absolute; }
  .menu-title {
    position: absolute; left: 0; width: 400px; top: 290px; text-align: center;
    font-family: "League Spartan", sans-serif; font-weight: 800; font-size: 66px; letter-spacing: -1px;
    color: var(--white); text-shadow: -4px 3px 0 var(--ink);
    line-height: 1;
  }
  .menu-column { position: absolute; top: 406px; }
  .menu-column.left { left: 12px; width: 186px; }
  .menu-column.right { left: 208px; width: 186px; }
  .menu-item { position: absolute; left: 0; width: 100%; }
  .item-head {
    display: flex; align-items: baseline;
    font-family: "Fjalla One", sans-serif; font-size: 14.5px; color: var(--orange); letter-spacing: .3px;
  }
  .item-head::before {
    content: ""; width: 4px; height: 4px; border-radius: 50%; background: var(--ink);
    margin-right: 4px; align-self: center;
  }
  .leader { flex: 1; border-bottom: 1.5px dotted var(--ink); margin: 0 2px; transform: translateY(-3px); }
  .price { color: var(--orange); }
  .item-desc {
    font-family: "Didact Gothic", sans-serif; font-size: 9px; line-height: 12px; color: var(--ink);
    padding-left: 8px; margin-top: 2px;
  }
  .sauces-title {
    position: absolute; left: 0; width: 400px; top: 623px; text-align: center;
    font-family: "Fjalla One", sans-serif; font-size: 38px; color: var(--white);
    text-shadow: -3px 2px 0 var(--ink); line-height: 1;
  }
  .sauce {
    position: absolute; font-family: "Fjalla One", sans-serif; font-size: 17px; color: var(--white);
    display: flex; align-items: center; line-height: 1; letter-spacing: .3px;
  }
  .sauce::before {
    content: ""; width: 7px; height: 7px; border-radius: 50%; background: var(--ink); margin-right: 4px;
  }
</style>
</head>
<body>
<main class="menu-board">
  <svg class="photo-arc" width="400" height="290" viewBox="0 0 400 290">
    <path d="M113 62 C 60 130, 95 230, 250 278 C 300 285, 350 265, 370 230" fill="none" stroke="var(--orange)" stroke-width="4"/>
  </svg>
  <svg class="photo hero-photo" viewBox="0 0 280 272" role="img" aria-label="Photo of a grilled chicken wrap cut in half, filled with greens, tomato and red onion">
    <defs>
      <linearGradient id="heroTone" x1="0" y1="0" x2="1" y2="1">
        <stop offset="0" stop-color="#e9d6b0"/>
        <stop offset=".45" stop-color="#7a9c3e"/>
        <stop offset=".7" stop-color="#c9553a"/>
        <stop offset="1" stop-color="#e4c48e"/>
      </linearGradient>
    </defs>
    <path d="M90 0 H280 V272 H200 C 120 250, 40 170, 60 60 C 66 35, 76 15, 90 0 Z" fill="url(#heroTone)"/>
  </svg>
  <div class="photo dish-photo photo-potatoes" role="img" aria-label="Photo of golden roasted potatoes"></div>
  <div class="photo dish-photo photo-ciabatta" role="img" aria-label="Photo of a chicken ciabatta sandwich"></div>
  <div class="photo dish-photo photo-wrap" role="img" aria-label="Photo of a toasted slaw wrap"></div>
  <div class="photo dish-photo photo-roast" role="img" aria-label="Photo of roasted potatoes with rosemary"></div>
  <div class="photo dish-photo photo-chicken" role="img" aria-label="Photo of roast chicken with veggie rice"></div>

  <svg class="brush" style="left:24px;top:278px" width="352" height="108" viewBox="0 0 352 108">
    <path d="M30 18 L120 10 L200 4 L300 10 L338 14 L322 22 L348 30 L330 40 L344 52 L326 62 L340 72 L320 84 L300 92 L220 100 L140 104 L70 98 L40 90 L58 82 L20 74 L6 62 L28 54 L2 44 L24 34 L12 26 Z" fill="var(--orange)"/>
    <path d="M60 20 L10 22 M300 96 L346 98 M80 102 L30 104" stroke="var(--orange)" stroke-width="2"/>
  </svg>
  <h1 class="menu-title">MENU</h1>

  <section class="menu-column left">
    <div class="menu-item" style="top:0">
      <div class="item-head">CIABATTA<span class="leader"></span><span class="price">£6</span></div>
      <p class="item-desc">Roti Chicken, Rucola, Caramelized<br>Onions, Tomato, Fresh Onion</p>
    </div>
    <div class="menu-item" style="top:53px">
      <div class="item-head">WRAP<span class="leader"></span><span class="price">£7</span></div>
      <p class="item-desc">Roti Chicken, Cruncgy Slaw, Tomato,<br>Fresh Onion &amp; Sauce of your choice</p>
    </div>
    <div class="menu-item" style="top:116px">
      <div class="item-head">BEETROOT WRAP<span class="leader"></span><span class="price">£8</span></div>
      <p class="item-desc">Roti Chicken, Cruncgy Slaw, Tomato,<br>Fresh Onion &amp; Sauce of your choice</p>
    </div>
  </section>

  <section class="menu-column right">
    <div class="menu-item" style="top:0">
      <div class="item-head">1/4 CHICKEN BOX<span class="leader"></span><span class="price">£9</span></div>
      <p class="item-desc">Roti Chicken, Veggie Rice &amp; Salad</p>
    </div>
    <div class="menu-item" style="top:41px">
      <div class="item-head">1/2 CHICKEN BOX<span class="leader"></span><span class="price">£14</span></div>
      <p class="item-desc">Roti Chicken, Veggie Rice &amp; Salad</p>
    </div>
    <div class="menu-item" style="top:82px">
      <div class="item-head">ROASTED POTAOES<span class="leader"></span><span class="price">£2.5</span></div>
      <p class="item-desc">Thyme &amp; Garlic</p>
    </div>
    <div class="menu-item" style="top:123px">
      <div class="item-head">WATER<span class="leader"></span><span class="price">£1</span></div>
    </div>
    <div class="menu-item" style="top:151px">
      <div class="item-head">CAN &amp; JUICES<span class="leader"></span><span class="price">£1.8</span></div>
    </div>
  </section>

  <svg class="brush" style="left:30px;top:594px" width="350" height="200" viewBox="0 0 350 200">
    <path d="M40 12 L140 6 L250 4 L310 10 L300 20 L326 28 L312 40 L330 52 L318 70 L336 86 L324 104 L340 122 L328 140 L344 156 L330 168 L300 178 L220 186 L140 190 L70 184 L40 176 L58 166 L28 156 L44 142 L14 128 L34 114 L4 100 L26 86 L18 70 L36 56 L24 40 L46 28 L30 20 Z" fill="var(--orange)"/>
    <path d="M60 2 L300 0 M30 192 L320 196" stroke="var(--orange)" stroke-width="2" stroke-dasharray="14 6"/>
  </svg>
  <h2 class="sauces-title">SAUCES</h2>
  <ul class="sauce-list">
    <li class="sauce" style="left:72px;top:678px">SIGNATURE</li>
    <li class="sauce" style="left:248px;top:678px">PIRI PIRI</li>
    <li class="sauce" style="left:181px;top:702px">BBQ</li>
    <li class="sauce" style="left:58px;top:730px">SWEET CHILLI</li>
    <li class="sauce" style="left:229px;top:730px">GARLIC MAYO</li>
  </ul>
</main>
</body>
</html>
```